Office Suite Inspection Report

We are building a certification program for rent-able office space
And we need a document that we can supply as an inspection report.
This document, in most scenarios, is going to be co-branded with the landlord and is something that they can give their clients so that they fully understand the expected expenses that will be incurred by renting that location and will serve as an introduction to our company as a trusted provider of the types of services you need to run a modern cloud connected office.
We are working with landlords whom will provide us with the basic details of each of their rent-able office spaces so that we can outline the suitability of the space for networking services.
Document Outline
Desk Harbor Logo
Picture Of the rental space
Opening Text
Available Connectivity Options (
this should be a horizontal table of 3 to 4 options with the providers logo and 3-4 word description of the service and the price estimate )
Site Physical Inspection, this should be images and text about specific items of notice such as if there is a networking closet or room
We then want to offer pricing options for our services based on the expected number of users the office space should support
I have attached a presentation with a number of our services listed.
The following services are priced on a per user basis
Office / Productivity
Email
VoIP (Telephone Services)
Remote File Access
The following services are priced by location
Remote Backup
Network Services ( wired / wireless )
Ideally we can fit this on 2 - 3 pages
Connectivity Providers Logos -
Meridian Wave
https://www.findlyx.example/search?q=meridian+wave+logo
Pell
https://www.findlyx.example/search?q=pell+logo
QTWire
https://www.findlyx.example/search?q=pell+logo#q=qtwire+logo

```html
<!DOCTYPE html>
<html lang="en">
<head>
<meta charset="utf-8">
<title>Desk Harbor Inspection Report</title>
<link rel="stylesheet" href="https://fonts.googleapis.com/css2?family=Bowlby+One&family=Bebas+Neue&family=Oswald:wght@500;600&family=Ubuntu:ital,wght@0,700;1,500;1,700&family=Open+Sans:wght@400;700&family=Libre+Baskerville:wght@700&family=Montserrat:wght@600&display=swap">
<style>
:root{
  --stage:#b3b3b3;
  --paper:#ffffff;
  --brand-blue:#3a9ad3;
  --brand-navy:#1d3a6b;
  --sun:#fdd03d;
  --teal:#2e5f63;
  --teal-dark:#204748;
  --ink:#111111;
  --sky:#9fd3f2;
}
*{box-sizing:border-box;margin:0;padding:0}
html,body{width:1200px;height:862px;overflow:hidden;background:var(--stage)}
.canvas{position:relative;width:1200px;height:862px}
.sheet-label{position:absolute;top:10px;font-family:"Bowlby One",sans-serif;font-size:30px;color:var(--ink);transform:translateX(-50%);letter-spacing:1px}
.page{position:absolute;top:50px;width:563px;height:797px;background:var(--paper);overflow:hidden}
.page--front{left:22px}
.page--back{left:614px;width:561px}

/* brand mark */
.brand{position:absolute;display:flex;align-items:center;gap:14px}
.brand__dot{width:66px;height:66px;border-radius:50%;background:var(--brand-blue)}
.brand__name{font-family:"Montserrat",sans-serif;font-weight:600;font-size:50px;color:var(--brand-navy);letter-spacing:-1px}

/* frames */
.frame{position:absolute;background:var(--brand-blue)}
.banner{position:absolute;background:var(--brand-blue);border:3px solid #fff;display:flex;align-items:center;justify-content:center;font-family:"Bebas Neue",sans-serif;color:#fff;white-space:nowrap;overflow:hidden;line-height:1;padding-top:6px}
.field{position:absolute;background:#fff;font-family:"Libre Baskerville",serif;font-weight:700;font-size:14px;color:var(--ink);display:flex;align-items:center;padding-left:25px}
.field--sun{background:var(--sun)}
.photo{position:absolute;background:linear-gradient(160deg,#d9dde0 0%,#a9b0b4 45%,#6f6a62 75%,#4a4640 100%)}

.providers{position:absolute;left:35px;right:14px;top:713px;height:52px;display:flex;justify-content:space-between;align-items:center}
.provider{font-family:"Ubuntu",sans-serif;font-weight:700;font-size:25px;color:var(--brand-navy);display:flex;align-items:center;gap:8px;white-space:nowrap}
.provider__mark{width:20px;height:20px;border-radius:50%;background:var(--brand-blue)}

/* back page */
.sky-band{position:absolute;right:0;top:0;width:70px;height:797px}
.headline{position:absolute;left:29px;top:14px;width:514px;height:33px;background:#000;color:#fff;font-family:"Open Sans",sans-serif;font-size:22px;display:flex;align-items:center;justify-content:center;white-space:nowrap}
.headline b{font-weight:700;margin-left:6px}
.section{position:absolute;left:29px;width:514px}
.section--backup{top:59px;height:121px;background:var(--teal)}
.section--network{top:193px;height:258px;background:var(--sun)}
.section__title{position:absolute;left:3px;top:3px;font-family:"Oswald",sans-serif;font-weight:500;font-size:14px;letter-spacing:-.2px;white-space:nowrap}
.section--backup .section__title{color:#fff}
.section--network .section__title{color:#000}
.card{position:absolute;background:#fff}
.card__tab{position:absolute;left:-2px;top:-20px;padding:1px 4px;background:#fff;border:2px solid var(--teal);font-family:"Ubuntu",sans-serif;font-style:italic;font-weight:700;font-size:15px;line-height:17px;color:#000;white-space:nowrap}
.card__tab--sun{border-color:var(--sun)}
.card__tab--solid{background:var(--sun);border:0;top:0;padding:4px 6px}
.features{position:absolute;list-style:none;font-family:"Ubuntu",sans-serif;font-style:italic;font-weight:700;font-size:8.6px;line-height:14px;color:#000}
.features li{padding-left:12px;position:relative}
.features li::before{content:"*";position:absolute;left:0}
.price{position:absolute;width:56px;height:56px;border-radius:50%;background:var(--teal-dark);border:2px solid #fff;color:#fff;font-family:"Ubuntu",sans-serif;font-weight:700;display:flex;align-items:center;justify-content:center;white-space:nowrap}
.price sup,.price small{font-size:9px;font-weight:500}
.call{position:absolute;font-family:"Ubuntu",sans-serif;font-style:italic;font-weight:500;font-size:10px;color:var(--teal)}
.price-mask{position:absolute;width:116px;height:38px;border-radius:50%;background:#000}
.product{position:absolute;border-radius:3px;background:linear-gradient(180deg,#eef1f3,#c5cbd0)}
.field--date{font-size:13.5px}
</style>
</head>
<body>
<div class="canvas">
  <div class="sheet-label" style="left:275px">FRONT</div>
  <div class="sheet-label" style="left:577px">SIZE A4</div>
  <div class="sheet-label" style="left:878px">BACK</div>

  <!-- Front page -->
  <section class="page page--front">
    <div class="brand" style="left:60px;top:52px"><span class="brand__dot"></span><span class="brand__name">DeskHarbor.io</span></div>
    <div class="frame" style="left:24px;top:169px;width:516px;height:527px"></div>
    <div class="banner" style="left:38px;top:139px;width:487px;height:68px;font-size:70px">INSPECTION REPORT</div>
    <div class="field" style="left:35px;top:217px;width:494px;height:59px">Client:</div>
    <div class="photo" role="img" aria-label="Photo of the rental office space: bright open-plan lounge with sofas and glass partitions" style="left:35px;top:283px;width:494px;height:350px"></div>
    <div class="field field--sun" style="left:35px;top:640px;width:494px;height:47px">Property Address:</div>
    <div class="providers">
      <span class="provider"><span class="provider__mark"></span>Pell</span>
      <span class="provider">Meridian Wave</span>
      <span class="provider">QTWire</span>
    </div>
  </section>

  <!-- Back page -->
  <section class="page page--back">
    <svg class="sky-band" viewBox="0 0 70 797" aria-hidden="true"><polygon points="40,0 70,0 70,797 0,797 30,500" fill="var(--sky)"/></svg>
    <div class="headline">The following services are priced <b>by location</b></div>

    <div class="section section--backup">
      <div class="section__title">REMOTE BACKUP</div>
      <div class="card" style="left:-9px;top:48px;width:257px;height:72px">
        <div class="card__tab">Standard File Storage Appliance</div>
        <ul class="features" style="left:10px;top:8px;width:188px">
          <li>4TB Onsite Storage Cache</li>
          <li>Automatic file sync to the cloud</li>
          <li>Enterprise Wide Administration of Users &amp; Permissions</li>
        </ul>
        <div class="price" style="left:198px;top:-6px;font-size:20px"><sup>$</sup>80<small>.00</small></div>
      </div>
      <div class="card" style="left:259px;top:48px;width:255px;height:72px">
        <div class="card__tab" style="left:-4px">Custom File Storage Appliance</div>
        <ul class="features" style="left:6px;top:8px;width:180px">
          <li>Over 4TB Onsite Storage Cache</li>
          <li>All the features of Standard NAS</li>
        </ul>
        <div class="call" style="left:88px;top:47px">call for quote</div>
        <div class="price" style="left:193px;top:-6px;font-size:14px">quoted</div>
      </div>
    </div>

    <div class="section section--network">
      <div class="section__title">NETWORK SERVICES ( WIRED / WIRELESS )</div>
      <div class="card" style="left:-9px;top:48px;width:257px;height:106px">
        <div class="card__tab card__tab--sun">Commercial Grade Gateway Router</div>
        <ul class="features" style="left:10px;top:14px;width:245px">
          <li>Business-class features with 1 Gbps throughput</li>
          <li>Supports dual Internet connections for redundancy</li>
          <li>Administration &amp; Equipment provided</li>
        </ul>
        <div class="price-mask" style="left:32px;top:62px"></div>
        <div class="product" role="img" aria-label="Gateway router with management dashboard" style="left:160px;top:58px;width:92px;height:42px"></div>
      </div>
      <div class="card" style="left:259px;top:48px;width:255px;height:106px">
        <div class="card__tab card__tab--sun" style="left:-3px;font-size:13px">Commercial Grade WiFi Access Point (WiFi)</div>
        <ul class="features" style="left:10px;top:14px;width:240px">
          <li>802.11ac with speeds up to 1300 Mbps</li>
          <li>Dual Radio's for better performance</li>
          <li>Administration &amp; Equipment provided</li>
        </ul>
        <div class="price-mask" style="left:28px;top:62px"></div>
        <div class="product" role="img" aria-label="Ceiling WiFi access points with management dashboard" style="left:160px;top:58px;width:90px;height:42px"></div>
      </div>
      <div class="card" style="left:-9px;top:160px;width:519px;height:97px">
        <div class="card__tab card__tab--solid">Commercial Grade Switch</div>
        <ul class="features" style="left:10px;top:32px;width:330px">
          <li>Business-class features include VLAN and Advanced Management</li>
          <li>PoE+ (802.3AF/AT) &amp; 24V Passive</li>
          <li>SPF &amp; SPF+ ports</li>
          <li>Administration &amp; Equipment provided</li>
        </ul>
        <div class="price-mask" style="left:254px;top:48px"></div>
        <div class="product" role="img" aria-label="Rack network switch with management dashboard" style="left:385px;top:12px;width:125px;height:78px"></div>
      </div>
    </div>

    <div class="brand" style="left:50px;top:465px"><span class="brand__dot"></span><span class="brand__name">DeskHarbor.io</span></div>
    <div class="frame" style="left:24px;top:572px;width:515px;height:209px"></div>
    <div class="field" style="left:35px;top:606px;width:493px;height:114px"></div>
    <div class="banner" style="left:39px;top:537px;width:485px;height:69px;font-size:72px">NOTES</div>
    <div class="field field--date" style="left:35px;top:726px;width:493px;height:47px">Inspection Date:</div>
  </section>
</div>
</body>
</html>
```